Business card design needed

My business is called The Driftwood Nook it is a small wine bar/cafe in the coastal town of Ocean Grove. We have great homestyle food, live acoustic music and a great range of beer wine and spirits. We are also available for private functions

Target Market(s)

Our market are people aged from 25 to 60

Industry/Entity Type

Town

Contact Information for Business Card

The Driftwood Nook
Shop 8 47 Marlow Parade
Pelham Cove Victoria 3999

Harvey Pellman
03 59418276
0438172604
email driftwoodnookbay@mailbox-example.net

Requirements
Must have
• Black glossy card with gold writing

```html
<!DOCTYPE html>
<html lang="en">
<head>
<meta charset="utf-8">
<title>The Driftwood Nook Shop – Business Card</title>
<link rel="stylesheet" href="https://fonts.googleapis.com/css2?family=Quicksand:wght@400&family=Marcellus&display=swap">
<style>
  :root {
    --backdrop: #2b2b2b;
    --card-top: #2a2a2a;
    --card-bottom: #050505;
    --gold: #d9b54a;
    --text-light: #e6e6e6;
    --icon-ring: #cfcfcf;
  }
  * { margin: 0; padding: 0; box-sizing: border-box; }
  html, body {
    width: 1200px;
    height: 861px;
    overflow: hidden;
    background: var(--backdrop);
  }
  .stage {
    width: 1200px;
    height: 861px;
    display: flex;
    align-items: center;
    justify-content: center;
  }
  .business-card {
    position: relative;
    width: 900px;
    height: 514px;
    border-radius: 22px;
    background: linear-gradient(160deg, var(--card-top) 0%, #121212 45%, var(--card-bottom) 100%);
    box-shadow: 0 18px 40px rgba(0, 0, 0, 0.55);
    overflow: hidden;
  }
  .business-name {
    position: absolute;
    top: 74px;
    left: 0;
    right: 0;
    text-align: center;
    font-family: "Quicksand", sans-serif;
    font-weight: 400;
    font-size: 52px;
    color: var(--gold);
    white-space: nowrap;
  }
  .contact-list {
    position: absolute;
    left: 56px;
    top: 238px;
    list-style: none;
    font-family: "Quicksand", sans-serif;
    font-weight: 400;
    font-size: 23px;
    line-height: 29px;
    color: var(--text-light);
  }
  .contact-item {
    display: flex;
    align-items: flex-start;
    margin-bottom: 18px;
  }
  .contact-icon {
    flex: none;
    width: 30px;
    height: 30px;
    margin-right: 16px;
  }
  .contact-name {
    position: absolute;
    right: 56px;
    top: 315px;
    font-family: "Marcellus", serif;
    font-size: 44px;
    color: var(--text-light);
    white-space: nowrap;
  }
</style>
</head>
<body>
<main class="stage">
  <section class="business-card">
    <h1 class="business-name">The Driftwood Nook Shop</h1>

    <ul class="contact-list">
      <li class="contact-item">
        <svg class="contact-icon" viewBox="0 0 30 30" aria-hidden="true">
          <circle cx="15" cy="15" r="13" fill="none" stroke="var(--icon-ring)" stroke-width="2"/>
          <rect x="9" y="9" width="8" height="13" fill="var(--icon-ring)"/>
          <rect x="17" y="13" width="5" height="9" fill="var(--icon-ring)"/>
          <rect x="11" y="11" width="1.5" height="2" fill="#000"/>
          <rect x="14" y="11" width="1.5" height="2" fill="#000"/>
          <rect x="11" y="15" width="1.5" height="2" fill="#000"/>
          <rect x="14" y="15" width="1.5" height="2" fill="#000"/>
        </svg>
        <span>Shop 8 47 Marlow Parade Pelham Cove<br>Victoria 3999</span>
      </li>
      <li class="contact-item">
        <svg class="contact-icon" viewBox="0 0 30 30" aria-hidden="true">
          <circle cx="15" cy="15" r="13" fill="none" stroke="var(--icon-ring)" stroke-width="2"/>
          <path d="M10 20 L19 9 Q21 8 22 10 L13 21 Q11 22 10 20 Z" fill="var(--icon-ring)"/>
        </svg>
        <span>03 59418276</span>
      </li>
      <li class="contact-item">
        <svg class="contact-icon" viewBox="0 0 30 30" aria-hidden="true">
          <circle cx="15" cy="15" r="13" fill="none" stroke="var(--icon-ring)" stroke-width="2"/>
          <rect x="11" y="7" width="8" height="16" rx="1.5" fill="var(--icon-ring)"/>
          <rect x="12.5" y="9" width="5" height="5" fill="#000"/>
        </svg>
        <span>0438172604</span>
      </li>
      <li class="contact-item">
        <svg class="contact-icon" viewBox="0 0 30 30" aria-hidden="true">
          <circle cx="15" cy="15" r="13" fill="none" stroke="var(--icon-ring)" stroke-width="2"/>
          <rect x="8" y="10" width="14" height="10" fill="var(--icon-ring)"/>
          <path d="M8 10 L15 16 L22 10" fill="none" stroke="#000" stroke-width="1.5"/>
        </svg>
        <span>driftwoodnookbay@mailbox-example.net</span>
      </li>
    </ul>

    <p class="contact-name">Harvey Pellman</p>
  </section>
</main>
</body>
</html>
```